Design a blog page showing lists of latest posts.

I want to design my blog home page. This page will show a list of my latest blog posts.

The site URL is lumbero.com and I have already given a basic structure to it. Please visit and have a look at it.

The color scheme of the design should be black (or grey) and white.

Below the top header I want an opt-in form and below that list of my blog posts. Then pagination and then a bottom section, that will show my two products. Please design these two boxes without any image.

Please avoid using any background image. If necessary, use any image without a character or person. Avoid using the sidebar.

Make it beautiful with the use of typography and white spaces.

I am open to any new creative ideas. Let me know if you have any?

1 page

• Sidebar

```html
<!DOCTYPE html>
<html lang="en">
<head>
<meta charset="utf-8">
<title>Lumbero Study Circle – Blog</title>
<link rel="stylesheet" href="https://fonts.googleapis.com/css2?family=Poppins:wght@300;400;500;600;700&family=Roboto:wght@300;400;500;700&display=swap">
<style>
:root{
  --ink:#1c1c1c;
  --ink-soft:#2a2a2a;
  --text:#333;
  --muted:#777;
  --line:#dcdcdc;
  --hero-a:#ececec;
  --hero-b:#f7f7f7;
  --paper:#fff;
  --chip:#e6e6e6;
}
*{box-sizing:border-box;margin:0;padding:0}
html,body{width:1200px;height:3074px;overflow:hidden;background:var(--paper);font-family:'Poppins',sans-serif;color:var(--text)}
.page{position:relative;width:1200px;height:3074px}

/* header */
.site-header{position:absolute;top:0;left:0;width:1200px;height:84px;background:var(--ink);display:flex;align-items:center;padding:0 117px;justify-content:space-between}
.brand{display:flex;align-items:center;gap:10px;color:#fff;font-family:'Roboto',sans-serif;font-weight:500;font-size:25px}
.brand-dot{width:30px;height:30px;border-radius:50%;background:#bbb}
.main-nav{display:flex;gap:8px;align-items:center}
.main-nav a{color:#fff;text-decoration:none;font-size:15px;padding:8px 14px;border-radius:2px}
.main-nav a.active{background:#fff;color:var(--ink);text-decoration:underline;padding:8px 22px}

/* hero */
.hero{position:absolute;top:84px;left:0;width:1200px;height:510px;background:radial-gradient(ellipse at 70% 60%,var(--hero-b),var(--hero-a) 70%);text-align:center;font-family:'Roboto',sans-serif}
.hero h1{position:absolute;top:130px;width:100%;font-size:49px;font-weight:700;color:var(--ink);letter-spacing:-.5px}
.hero p{position:absolute;top:198px;width:100%;font-size:22px;font-weight:300;color:#222;line-height:37px}
.optin{position:absolute;top:311px;left:332px;width:536px;height:53px;display:flex}
.optin input{flex:1;border:1px solid #6d8cb0;background:#fff;padding:0 20px;font:16px 'Roboto',sans-serif;color:#666}
.optin button{width:181px;border:0;background:var(--ink-soft);color:#fff;font:17px 'Roboto',sans-serif}

/* posts */
.posts-head{position:absolute;top:650px;left:116px;width:966px;height:86px;border-bottom:1px solid var(--line)}
.posts-head h2{font-size:50px;font-weight:300;color:var(--ink);line-height:62px}
.posts-head h2 b{font-weight:700}
.search{position:absolute;right:0;top:12px;width:286px;height:42px;background:var(--chip);border-radius:4px;display:flex;align-items:center;justify-content:space-between;padding:0 22px;font-size:15px;color:#333}
.post-grid{position:absolute;top:779px;left:117px;width:966px;display:grid;grid-template-columns:repeat(3,305px);column-gap:25px;row-gap:28px}
.post-card{height:360px;background:#fff;box-shadow:0 2px 10px rgba(0,0,0,.07);border-radius:3px;overflow:hidden;font-family:'Poppins',sans-serif}
.post-thumb{height:218px;display:flex;align-items:center;justify-content:center;text-align:center;color:#fff;font-size:16px;font-weight:600;line-height:30px}
.post-meta{display:flex;justify-content:space-between;padding:24px 25px 0;font-size:11px;color:var(--muted)}
.post-title{padding:10px 22px 0 25px;font-size:17px;font-weight:600;color:var(--ink-soft);line-height:28px}
.t1{background:linear-gradient(135deg,#3fcf3a,#8ef07a)}
.t2{background:linear-gradient(160deg,#e8891a,#d9a57a 60%,#bdbdbd)}
.t3{background:linear-gradient(135deg,#eeeeee,#9aa3ad)}
.t4{background:linear-gradient(135deg,#1ba4e6,#35c8f7)}
.t5{background:linear-gradient(135deg,#f2f2f2,#c8c8c8)}
.t6{background:linear-gradient(180deg,#8a5a2a 0,#2f4f3a 8%,#22402e)}
.t7{background:radial-gradient(circle at 20% 30%,#5a1111,#15171f 70%)}
.t8{background:radial-gradient(circle at 50% 40%,#1f4fc0,#0b1f5c 75%)}
.t9{background:radial-gradient(circle at 40% 50%,#0f4a4a,#081c26 75%)}

/* pagination */
.pager{position:absolute;top:1977px;left:0;width:1200px;display:flex;justify-content:center;gap:7px}
.pager span{width:42px;height:42px;border-radius:50%;border:1px solid #ccc;display:flex;align-items:center;justify-content:center;font-size:14px;color:#888}
.pager .arrow{background:var(--chip);border-color:var(--chip);color:#333}
.pager .current{background:var(--ink-soft);border-color:var(--ink-soft);color:#fff}

/* resources */
.resources-head{position:absolute;top:2082px;left:0;width:1200px;text-align:center}
.resources-head h2{font-size:52px;font-weight:300;color:var(--ink);line-height:66px}
.resources-head h2 b{font-weight:700}
.resources-head p{margin-top:16px;font-size:18px;color:#555;line-height:30px}
.product{position:absolute;top:2257px;width:465px;height:347px;background:var(--ink-soft);border-radius:3px;color:#fff;text-align:center;padding-top:30px}
.product.left{left:122px}
.product.right{left:613px}
.product svg{display:block;margin:0 auto}
.product h3{margin-top:16px;font-size:19px;font-weight:400}
.product .by{font-size:13px;color:#ddd;margin-top:4px}
.product .desc{margin:20px auto 0;width:300px;font-size:13px;line-height:22px;color:#e4e4e4}
.product .btn{display:inline-block;margin-top:22px;background:#fff;color:var(--ink);font-size:16px;padding:8px 19px;border-radius:2px}
.hub{position:absolute;top:2360px;left:532px;width:132px;height:132px}

/* footer */
.site-footer{position:absolute;top:2706px;left:0;width:1200px;height:368px;background:var(--ink);color:#fff}
.foot-col{position:absolute;top:64px}
.foot-col h4{font-size:15px;font-weight:600}
.foot-col ul{list-style:none;margin-top:18px}
.about{left:117px;width:260px}
.about li{position:relative;padding-left:22px;font-size:14px;line-height:21px;margin-bottom:18px;color:#eee}
.about li::before{content:"";position:absolute;left:0;top:8px;width:6px;height:6px;background:#bbb}
.links{left:479px}
.links li{font-size:15px;line-height:25px;color:#eee}
.write{left:738px;width:340px}
.write h4{text-transform:uppercase;letter-spacing:.3px}
.write p{margin-top:18px;font-size:14px;line-height:25px;color:#eee}
.subscribe{display:flex;margin-top:40px;width:332px;height:38px;border-radius:19px;overflow:hidden;margin-left:-6px}
.subscribe span{flex:1;background:#eef1f6;color:#555;font-size:15px;padding:9px 24px}
.subscribe b{width:118px;background:#111;color:#fff;font-size:14px;font-weight:600;display:flex;align-items:center;justify-content:center}
.foot-bar{position:absolute;top:279px;left:0;width:1200px;border-top:1px solid #2c2c2c}
.copyright{position:absolute;top:305px;left:118px;font-size:13px;color:#ddd}
.social{position:absolute;top:300px;left:945px;display:flex;background:#2b2b2b;padding:6px 8px}
.social i{width:14px;height:14px;margin:0 6px;background:#999;display:block}
</style>
</head>
<body>
<div class="page">

  <header class="site-header">
    <div class="brand"><span class="brand-dot"></span>Lumbero Study Circle</div>
    <nav class="main-nav">
      <a class="active">Home</a><a>CPX Questions</a><a>Contact Hours</a><a>Resources</a><a>Notes</a><a>eBook</a>
    </nav>
  </header>

  <section class="hero">
    <h1>Never Miss a Post</h1>
    <p>In the online marketing space, everybody loves the quick win.<br>The shortcut. The "growth hack".</p>
    <form class="optin"><input value="Email Address" readonly><button type="button">Keep me updated</button></form>
  </section>

  <section class="posts-head">
    <h2>Latest <b>Posts...</b></h2>
    <div class="search">Search
      <svg width="12" height="8" viewBox="0 0 12 8"><path d="M1 1l5 5 5-5" fill="none" stroke="#333" stroke-width="1.4"/></svg>
    </div>
  </section>

  <main class="post-grid">
    <article class="post-card"><div class="post-thumb t1" role="img" aria-label="Green brain illustration with a crossed-out sign"></div>
      <div class="post-meta"><span>Omar Haddad</span><span>2 Comments</span></div>
      <h3 class="post-title">This is an Example of Sample Post</h3></article>
    <article class="post-card"><div class="post-thumb t2" role="img" aria-label="Orange world map banner for a training program"></div>
      <div class="post-meta"><span>Omar Haddad</span><span>2 Comments</span></div>
      <h3 class="post-title">30 Contact Hours Online RMX Training Programs</h3></article>
    <article class="post-card"><div class="post-thumb t3" role="img" aria-label="Improvement cycle diagram around a globe"></div>
      <div class="post-meta"><span>Omar Haddad</span><span>2 Comments</span></div>
      <h3 class="post-title">What is Lean Arc?</h3></article>

    <article class="post-card"><div class="post-thumb t4" role="img" aria-label="Blue banner comparing two certifications with globes and people"></div>
      <div class="post-meta"><span>Omar Haddad</span><span>2 Comments</span></div>
      <h3 class="post-title">Stride7 vs CPX</h3></article>
    <article class="post-card"><div class="post-thumb t5" role="img" aria-label="Desk scene with laptop, pen and phone for mock tests"></div>
      <div class="post-meta"><span>Omar Haddad</span><span>2 Comments</span></div>
      <h3 class="post-title">A List of Free CPX Mock Tests and Sample Questions</h3></article>
    <article class="post-card"><div class="post-thumb t6" role="img" aria-label="Chalkboard with lessons learned lettering and a teacher figure"></div>
      <div class="post-meta"><span>Omar Haddad</span><span>2 Comments</span></div>
      <h3 class="post-title">RMX Exam : Lessons Learned by Ravi Menon</h3></article>

    <article class="post-card"><div class="post-thumb t7" role="img" aria-label="Dark red network of glowing points">This is an Example of<br>Sample Post</div>
      <div class="post-meta"><span>Omar Haddad</span><span>2 Comments</span></div>
      <h3 class="post-title">This is an Example of Sample Post</h3></article>
    <article class="post-card"><div class="post-thumb t8" role="img" aria-label="Blue digital globe">This is an Example of<br>Sample Post</div>
      <div class="post-meta"><span>Omar Haddad</span><span>2 Comments</span></div>
      <h3 class="post-title">30 Contact Hours Online RMX Training Programs</h3></article>
    <article class="post-card"><div class="post-thumb t9" role="img" aria-label="Teal particle wave on dark background">This is an Example of<br>Sample Post</div>
      <div class="post-meta"><span>Omar Haddad</span><span>2 Comments</span></div>
      <h3 class="post-title">What is Lean Arc?</h3></article>
  </main>

  <nav class="pager">
    <span class="arrow">‹</span><span class="current">01</span><span>02</span><span>03</span><span>04</span><span class="arrow">›</span>
  </nav>

  <section class="resources-head">
    <h2>Top Recommended <b>Resources</b></h2>
    <p>Lorem ipsum dolor sit amet, consectetur adipiscing elit, sed do eiusmod<br>tempor incididunt ut labore et dolore magna aliqua.</p>
  </section>

  <article class="product left">
    <svg width="64" height="60" viewBox="0 0 64 60" fill="none" stroke="#fff" stroke-width="1.6">
      <rect x="2" y="8" width="60" height="40"/><circle cx="32" cy="8" r="5"/><path d="M24 48v-14h16v14M18 30h28M8 16h6M11 13v6M50 20h8"/><path d="M22 58h20"/>
    </svg>
    <h3>The CPX Training Program</h3>
    <div class="by">By Omar Haddad</div>
    <p class="desc">Lorem ipsum dolor sit amet, consectetur adipisicing elit, sed do eiusmod tempor incididunt ut labore et</p>
    <span class="btn">Read More</span>
  </article>

  <article class="product right">
    <svg width="64" height="60" viewBox="0 0 64 60" fill="none" stroke="#fff" stroke-width="1.6">
      <rect x="14" y="2" width="46" height="32"/><path d="M22 12h22M22 20h30M22 27h16"/><circle cx="14" cy="36" r="6"/><path d="M4 58v-8a10 10 0 0120 0v8M30 40h22v16H30z"/>
    </svg>
    <h3>The CPX Exam Preparation tool</h3>
    <div class="by">By Omar Haddad</div>
    <p class="desc">Lorem ipsum dolor sit amet, consectetur adipisicing elit, sed do eiusmod tempor incididunt ut labore et</p>
    <span class="btn">Read More</span>
  </article>

  <svg class="hub" viewBox="0 0 132 132">
    <circle cx="66" cy="66" r="64" fill="#fff" stroke="#222" stroke-width="1.5" stroke-dasharray="5 4"/>
    <circle cx="66" cy="66" r="44" fill="#f1f1f1"/>
    <circle cx="66" cy="66" r="26" fill="#9a9a9a"/>
  </svg>

  <footer class="site-footer">
    <div class="foot-col about"><h4>Lumbero Study Circle</h4>
      <ul><li>Lorem ipsum dolor sit amet consectetur adipisicing</li><li>Lorem ipsum dolor sit amet</li><li>Lorem ipsum dolor sit amet consectetur</li></ul></div>
    <div class="foot-col links"><h4>Quick Links</h4>
      <ul><li>Home</li><li>CPX</li><li>Contact Hours</li><li>Resources</li><li>Notes</li><li>ebook</li></ul></div>
    <div class="foot-col write"><h4>Write to us</h4>
      <p>Provide your email below to<br>subscribe to our newsletter</p>
      <div class="subscribe"><span>Email address</span><b>Subscribe</b></div></div>
    <div class="foot-bar"></div>
    <div class="copyright">Copyright 2020 lumbero. All rights reserved.</div>
    <div class="social"><i></i><i></i><i></i><i></i><i></i></div>
  </footer>

</div>
</body>
</html>
```